"VELORINE" is a pleasure enhancing cream for women

Need a simple rectangle box design and label for the bottle.
I have included lots of ideas and descriptions within my attachment.
It's a straight forward project. I've added more pic for inspiration.

Target Market(s)

Sex Industry, Massage Industry, Medical, Therapy industry, adult industry

Font styles to use
Sans Serif
Script

Requirements
Must have
• High-end look, quality and very sexy and I want to scream Lust
Nice to have
• The bottle needs to match package but be somewhat subliminal. More Infosys on the red lips and red fingernail the rest an outline
Should not have
• cartoon look

```html
<!DOCTYPE html>
<html lang="en">
<head>
<meta charset="utf-8">
<title>Velorine – Bottle and Box Packaging</title>
<link rel="stylesheet" href="https://fonts.googleapis.com/css2?family=Cinzel:wght@500;600;700&family=Roboto+Condensed:wght@400;700&family=Montserrat:wght@500;600&display=swap">
<style>
  :root {
    --canvas: #ffffff;
    --black: #0e0e0e;
    --charcoal: #1c1c1c;
    --gold: #c9a14a;
    --gold-light: #e6c877;
    --gold-dark: #8e6a22;
    --white: #ffffff;
    --frost: #eeeef3;
    --cap: #e4e4e8;
    --red: #c8141c;
    --skin: #d9a88f;
  }
  * { box-sizing: border-box; margin: 0; padding: 0; }
  html, body { width: 1200px; height: 1000px; overflow: hidden; background: var(--canvas); }
  .canvas { position: relative; width: 1200px; height: 1000px; background: var(--canvas); }

  .gold-rule { height: 1px; background: linear-gradient(90deg, var(--gold-dark), var(--gold-light), var(--gold-dark)); }
  .gold-text {
    background: linear-gradient(180deg, var(--gold-light), var(--gold) 55%, var(--gold-dark));
    -webkit-background-clip: text; background-clip: text; color: transparent;
  }
  .brand { font-family: "Cinzel", serif; font-weight: 600; letter-spacing: 0.5px; }
  .tag {
    display: inline-block; background: linear-gradient(180deg, var(--gold-light), var(--gold));
    color: var(--black); font-family: "Montserrat", sans-serif; font-weight: 500;
  }

  /* Bottle */
  .bottle { position: absolute; left: 408px; top: 125px; width: 144px; height: 680px; }
  .bottle-cap {
    position: absolute; left: 0; top: 0; width: 144px; height: 212px;
    background: linear-gradient(90deg, #d7d7dc, var(--cap) 40%, #f5f5f7 60%, #d2d2d8);
    border-radius: 8px 8px 0 0;
  }
  .bottle-pump {
    position: absolute; left: 32px; top: 20px; width: 80px; height: 192px;
    background: linear-gradient(90deg, #111, #3a3a3a 50%, #111); border-radius: 4px 4px 0 0;
  }
  .bottle-band { position: absolute; left: 0; top: 208px; width: 144px; height: 20px;
    background: linear-gradient(180deg, var(--gold-dark), var(--gold-light) 50%, var(--gold-dark)); }
  .bottle-label {
    position: absolute; left: 0; top: 228px; width: 144px; height: 360px;
    background: linear-gradient(90deg, #e2e2ea, var(--frost) 45%, #f7f7fa 60%, #dcdce4);
    text-align: center; padding-top: 40px;
  }
  .bottle-label .brand { font-size: 14px; color: var(--black); }
  .bottle-label .gold-rule { width: 110px; margin: 4px auto 0; }
  .bottle-art {
    width: 118px; height: 210px; margin: 6px auto 0;
    background: radial-gradient(ellipse 50% 14% at 50% 14%, var(--red) 70%, transparent 72%),
                radial-gradient(ellipse 40% 55% at 45% 55%, rgba(201,161,74,0.35), transparent 70%);
  }
  .bottle-label .product { font-family: "Cinzel", serif; font-weight: 700; font-size: 19px; margin-top: 2px; }
  .bottle-label .tag { font-size: 9px; padding: 1px 6px; }
  .bottle-label .net { font-family: "Montserrat", sans-serif; font-size: 9px; color: var(--black); margin-top: 22px; }
  .bottle-base { position: absolute; left: 0; top: 588px; width: 144px; height: 92px;
    background: linear-gradient(90deg, #050505, #2a2a2a 50%, #050505); border-radius: 0 0 4px 4px; }

  /* Box */
  .box { position: absolute; top: 110px; height: 695px; background: radial-gradient(ellipse at 40% 30%, #262626, var(--black) 70%); }
  .box::after { content: ""; position: absolute; left: 0; right: 0; bottom: 0; height: 10px;
    background: linear-gradient(180deg, var(--gold-dark), var(--gold-light)); }
  .box::before { content: ""; position: absolute; left: 0; right: 0; top: 0; height: 6px;
    background: linear-gradient(180deg, var(--gold-light), var(--gold-dark)); }

  .box-front { left: 548px; width: 167px; }
  .box-front .header { position: absolute; left: 0; right: 0; top: 40px; text-align: center; }
  .box-front .header .gold-rule { width: 140px; margin: 0 auto; }
  .box-front .header .brand { font-size: 22px; color: var(--white); padding: 6px 0; }
  .box-front .photo {
    position: absolute; left: 0; right: 0; top: 118px; height: 430px;
    background: radial-gradient(ellipse 55% 40% at 50% 35%, var(--skin), #b47c64 60%, #6a4434);
  }
  .box-front .divider { position: absolute; left: 0; right: 0; top: 548px; height: 12px; background: #4a4a4a; }
  .box-front .footer { position: absolute; left: 0; right: 0; top: 570px; text-align: center; }
  .box-front .product { font-family: "Cinzel", serif; font-weight: 700; font-size: 26px; }
  .box-front .tag { font-size: 12px; padding: 2px 8px; margin-top: 4px; }
  .box-front .net { font-family: "Montserrat", sans-serif; font-weight: 600; font-size: 11px; color: var(--white); margin-top: 20px; }

  .box-side { left: 715px; width: 137px; background: linear-gradient(90deg, #090909, #1a1a1a 60%, #101010); }
  .box-side .ingredients { position: absolute; left: 10px; right: 8px; top: 42px; font-family: "Roboto Condensed", sans-serif; color: var(--white); }
  .box-side .ingredients h2 { font-size: 12px; font-weight: 700; }
  .box-side .ingredients p { font-size: 12px; line-height: 16px; text-align: justify; margin-top: 2px; }
  .box-side .maker { position: absolute; left: 10px; right: 8px; top: 522px; font-family: "Roboto Condensed", sans-serif; color: var(--white); }
  .box-side .maker .brand { font-size: 15px; }
  .box-side .maker .gold-rule { width: 96px; margin: 4px 0 10px; }
  .box-side .maker h3 { font-size: 10px; font-weight: 700; line-height: 13px; }
  .box-side .maker p { font-size: 10px; line-height: 16px; margin-top: 4px; }
</style>
</head>
<body>
<main class="canvas">

  <section class="bottle" aria-label="Velorine bottle label">
    <div class="bottle-cap"></div>
    <div class="bottle-pump"></div>
    <div class="bottle-band"></div>
    <div class="bottle-label">
      <div class="brand">SILK REVERIE</div>
      <div class="gold-rule"></div>
      <div class="bottle-art" role="img" aria-label="Red glossy lips with a gold line-drawn hand holding a finger to them"></div>
      <div class="product gold-text">VELORINE</div>
      <span class="tag">FOR WOMEN</span>
      <div class="net">Net 30ml</div>
    </div>
    <div class="bottle-base"></div>
  </section>

  <section class="box box-front" aria-label="Box front panel">
    <header class="header">
      <div class="gold-rule"></div>
      <div class="brand">SILK REVERIE</div>
      <div class="gold-rule"></div>
    </header>
    <div class="photo" role="img" aria-label="Photograph of a woman with red lips holding a finger to her lips"></div>
    <div class="divider"></div>
    <div class="footer">
      <div class="product gold-text">VELORINE</div>
      <span class="tag">FOR WOMEN</span>
      <div class="net">Net 30ml</div>
    </div>
  </section>

  <section class="box box-side" aria-label="Box side panel">
    <div class="ingredients">
      <h2>INGREDIENTS:</h2>
      <p>Lorem ipsum color sit amet, consectetur adipiscing elit, sed do eiusmod tempor inci didunt ut labore et dolore magna aliqua. Quis ipsum suspendisse ultrices gravida. Risus commodo viverra mae cenas accumsan lacus vel facilisis.</p>
    </div>
    <div class="maker">
      <div class="brand">SILK REVERIE</div>
      <div class="gold-rule"></div>
      <h3>MANUFACTURED FOR AND DISTRIBUTED BY:</h3>
      <p>LOREM IPSUM<br>123 A. Bcd Rd St 456<br>Lorem, Ipsum 7890<br>www.silkreverie.co</p>
    </div>
  </section>

</main>
</body>
</html>
```